Book Cover for self help book describing how to become the author of your life

I need a good resolution front cover for a book that is published through Brindlewick in Print and ebook format. I can design the spine and back cover myself so just need the front angle.
The book is titled "Chart New Mornings" and it's about writing your own story for how you want to live your life. The image I had in my mind was a pen writing out the title on the front in a script-like font, like actual handwriting.
I've included a very basic mock-up that I've done myself just to give the general idea. The cover requires three pieces of writing.
Title: Chart New Mornings
Subtitle: Step Into a Brighter Season
Author: Martin Olsfield
Female 35-55

```html
<!DOCTYPE html>
<html lang="en">
<head>
<meta charset="utf-8">
<title>Chart New Mornings — Martin Olsfield</title>
<link href="https://fonts.googleapis.com/css2?family=Great+Vibes&family=Allura&family=Almendra:wght@700&display=swap" rel="stylesheet">
<style>
  :root {
    --paper: #f7f7f9;
    --sage: #dde2cf;
    --sage-edge: #cdd5bd;
    --lavender: #c8c8de;
    --lavender-edge: #b9b9d3;
    --blush: #ddcdcc;
    --blush-edge: #d2bfbe;
    --table: #e8e3db;
    --ink: #363434;
    --photo-light: #e9d3c6;
    --photo-mid: #d2a98f;
    --photo-dark: #a87a62;
  }
  * { margin: 0; padding: 0; box-sizing: border-box; }
  html, body { width: 812px; height: 1200px; overflow: hidden; background: var(--paper); }
  .cover { position: relative; width: 812px; height: 1200px; overflow: hidden; background: var(--paper); }
  .bands { position: absolute; inset: 0; }
  .title {
    position: absolute; left: 0; top: 40px; width: 100%;
    font-family: "Great Vibes", cursive; font-weight: 400; color: var(--ink);
    text-align: center; line-height: 150px; font-size: 168px;
  }
  .title span { display: block; }
  .title .line-3 { font-size: 150px; }
  .subtitle {
    position: absolute; left: 0; top: 702px; width: 100%;
    font-family: "Almendra", serif; font-weight: 700; font-size: 46px;
    letter-spacing: 2px; color: var(--ink); text-align: center;
  }
  .author {
    position: absolute; left: 130px; top: 878px;
    font-family: "Allura", cursive; font-size: 68px; color: var(--ink);
  }
  .hand-photo { position: absolute; left: 560px; top: 820px; width: 252px; height: 380px; }
</style>
</head>
<body>
<main class="cover">
  <svg class="bands" width="812" height="1200" viewBox="0 0 812 1200" aria-hidden="true">
    <rect class="table-edge" x="0" y="1072" width="812" height="128" fill="var(--table)"/>
    <path class="sage-band" fill="var(--sage)"
      d="M0 10 L60 14 L120 6 L200 18 L280 8 L360 20 L440 12 L520 22 L600 10 L680 18 L760 8 L812 14
         L812 600 L760 598 L700 590 L640 604 L560 596 L480 610 L400 602 L320 614 L260 606 L200 618 L180 596 L150 600 L90 608 L30 600 L0 606 Z"/>
    <path class="sage-edge" fill="none" stroke="var(--sage-edge)" stroke-width="3"
      d="M0 10 L60 14 L120 6 L200 18 L280 8 L360 20 L440 12 L520 22 L600 10 L680 18 L760 8 L812 14"/>
    <path class="lavender-band" fill="var(--lavender)"
      d="M0 652 L80 646 L160 654 L240 648 L320 656 L400 650 L480 658 L560 650 L640 656 L720 648 L812 654
         L812 806 L740 812 L660 804 L580 814 L500 806 L420 814 L340 808 L260 816 L180 808 L100 814 L0 808 Z"/>
    <path fill="none" stroke="var(--lavender-edge)" stroke-width="3"
      d="M0 652 L80 646 L160 654 L240 648 L320 656 L400 650 L480 658 L560 650 L640 656 L720 648 L812 654"/>
    <path class="blush-band" fill="var(--blush)"
      d="M0 862 L90 858 L180 866 L270 860 L360 868 L450 862 L540 868 L630 860 L720 866 L812 862
         L812 996 L720 1002 L630 994 L540 1004 L450 996 L360 1004 L270 998 L180 1006 L90 998 L0 1004 Z"/>
    <path fill="none" stroke="var(--blush-edge)" stroke-width="3"
      d="M0 862 L90 858 L180 866 L270 860 L360 868 L450 862 L540 868 L630 860 L720 866 L812 862"/>
  </svg>

  <h1 class="title">
    <span class="line-1">Chart</span>
    <span class="line-2">New</span>
    <span class="line-3">Mornings</span>
  </h1>

  <p class="subtitle">Step Into a Brighter Season</p>

  <p class="author">Martin Olsfield</p>

  <svg class="hand-photo" viewBox="0 0 252 380" role="img" aria-label="Photograph of a hand holding a pencil, writing the author name on the page">
    <defs>
      <linearGradient id="photoTone" x1="0" y1="0" x2="1" y2="1">
        <stop offset="0" stop-color="var(--photo-light)"/>
        <stop offset="0.5" stop-color="var(--photo-mid)"/>
        <stop offset="1" stop-color="var(--photo-dark)"/>
      </linearGradient>
    </defs>
    <rect x="0" y="0" width="252" height="380" rx="10" fill="url(#photoTone)"/>
  </svg>
</main>
</body>
</html>
```